Meridian Dash add on sales tool2017

This will be a flyer to leave with our clients we just did work for. We want to entice them to use our other services over the next 30 days with a discount, money off etc. we will write in the special and the expiration date. I want the client to read the description and see a picture of the service they may want done.

Target Market(s)

Repeat clients

Industry/Entity Type

Cleaning Service

Font styles to use
Serif
Sans Serif

Colors
ec1f27
000000
b1b1b1

Requirements
Must have
• Call to action! look high end market, clients show we do 1st class work.
• Don't Waite
Nice to have
• Classy, quality, I'm open to using other pictures that may look better
Should not have
• Look like a typical carpet cleaners special flyer
• Not to look cluttered

```html
<!DOCTYPE html>
<html lang="en">
<head>
<meta charset="utf-8">
<title>Meridian Dash – 30 Day Special Offer</title>
<link href="https://fonts.googleapis.com/css2?family=Arimo:wght@400;700&family=Oswald:wght@600;700&family=Roboto+Slab:wght@700&display=swap" rel="stylesheet">
<style>
  :root {
    --brand-red: #ec1f27;
    --ink: #000000;
    --panel-grey: #b1b1b1;
    --ring-grey: #c9c9c9;
    --page-bg: #d6d6d6;
    --soap-light: #f4fbff;
    --soap-mid: #cfe9fa;
    --soap-deep: #9fd0f0;
    --body-text: #1a1a1a;
    --muted: #cfcfcf;
  }
  * { margin: 0; padding: 0; box-sizing: border-box; }
  html, body { width: 1200px; height: 1200px; overflow: hidden; background: var(--page-bg); }

  .flyer {
    position: absolute;
    left: 197px; top: 30px;
    width: 936px; height: 1324px;
    transform: scale(0.861);
    transform-origin: top left;
    background: #0b0b0b;
    overflow: hidden;
    font-family: "Arimo", Arial, sans-serif;
    box-shadow: 0 6px 18px rgba(0,0,0,0.25);
  }
  .flyer-backdrop { position: absolute; inset: 0; }

  .brand { position: absolute; left: 20px; top: 108px; width: 240px; text-align: center; }
  .brand-name { color: var(--brand-red); font-size: 26px; font-weight: 700; letter-spacing: 0.5px; }
  .brand-address { margin-top: 28px; color: var(--muted); font-size: 14px; line-height: 20px; }

  .offer-slot { position: absolute; left: 462px; top: 38px; width: 106px; height: 142px; background: #fff; border: 2px solid #222; }
  .offer-title { position: absolute; left: 578px; top: 28px; line-height: 1; }
  .offer-line { display: flex; align-items: baseline; white-space: nowrap; }
  .offer-num { font-family: "Oswald", sans-serif; font-weight: 700; color: var(--brand-red); font-size: 76px; letter-spacing: -2px; }
  .offer-word { font-family: "Oswald", sans-serif; font-weight: 700; color: var(--ink); font-size: 62px; margin-left: 6px; letter-spacing: -1px; }
  .offer-day { font-family: "Oswald", sans-serif; font-weight: 700; color: var(--brand-red); font-size: 56px; letter-spacing: -2px; }
  .offer-offer { font-family: "Arimo", sans-serif; font-weight: 400; color: var(--ink); font-size: 60px; margin-left: 2px; }
  .offer-phone { position: absolute; left: 580px; top: 158px; font-size: 20px; letter-spacing: 11px; color: var(--ink); }
  .offer-expires { position: absolute; left: 581px; top: 210px; font-size: 14px; color: var(--ink); }

  .headline {
    position: absolute; left: 236px; top: 266px;
    font-family: "Roboto Slab", Georgia, serif; font-weight: 700;
    font-size: 37px; line-height: 42px; color: var(--brand-red);
  }

  .cta-disc { position: absolute; left: 0; top: 0; width: 936px; height: 1324px; }
  .cta-text {
    position: absolute; left: 676px; top: 500px; width: 260px;
    text-align: center; color: #fff;
    font-size: 78px; line-height: 80px; font-weight: 400;
  }

  .service-photo {
    position: absolute; width: 184px; height: 184px; border-radius: 50%;
    border: 5px solid var(--panel-grey);
  }
  .photo-carpet { left: 34px; top: 350px; background: radial-gradient(circle at 60% 40%, #b8a183, #8a7558); }
  .photo-upholstery { left: 8px; top: 558px; background: linear-gradient(160deg, #a9ad9c, #6c6e5f 60%, #5b3f3a); }
  .photo-drapery { left: 34px; top: 760px; background: linear-gradient(90deg, #6b5446, #c9c6c0 55%, #8d8a86); }
  .photo-tile { left: 100px; top: 960px; background: linear-gradient(135deg, #8a8593, #a7a0a8 50%, #7d7378); }
  .photo-stone { left: 234px; top: 1110px; background: linear-gradient(180deg, #cfcfc8, #6f6b60 55%, #4f4b43); }

  .service { position: absolute; color: var(--body-text); }
  .service-title { font-size: 19px; font-weight: 700; line-height: 23px; }
  .service-copy { font-size: 18px; line-height: 23px; }
  .service-carpet { left: 236px; top: 397px; }
  .service-upholstery { left: 207px; top: 585px; }
  .service-drapery { left: 235px; top: 781px; }
  .service-tile { left: 307px; top: 989px; }
  .service-stone { left: 448px; top: 1136px; }
</style>
</head>
<body>
<main class="flyer">
  <svg class="flyer-backdrop" viewBox="0 0 936 1324" width="936" height="1324" role="img" aria-label="Soft blue soap bubble background">
    <defs>
      <radialGradient id="soap" cx="55%" cy="45%" r="75%">
        <stop offset="0" stop-color="var(--soap-light)"/>
        <stop offset="0.55" stop-color="var(--soap-mid)"/>
        <stop offset="1" stop-color="var(--soap-deep)"/>
      </radialGradient>
    </defs>
    <path d="M470 0 Q -230 660 440 1324 L 936 1324 L 936 0 Z" fill="url(#soap)"/>
    <path d="M470 0 Q -230 660 440 1324" fill="none" stroke="var(--brand-red)" stroke-width="16"/>
  </svg>

  <div class="brand">
    <div class="brand-name">MERIDIAN DASH</div>
    <div class="brand-address">418 W. Larkspur Ave. Suite C,<br>Silver Falls</div>
  </div>

  <div class="offer-slot"></div>
  <div class="offer-title">
    <div class="offer-line"><span class="offer-num">30</span><span class="offer-word">SPECIAL</span></div>
    <div class="offer-line"><span class="offer-day">DAY</span><span class="offer-offer">OFFER!</span></div>
  </div>
  <div class="offer-phone">555 314-2760</div>
  <div class="offer-expires">Expires.......................................................</div>

  <h1 class="headline">ONE STOP FOR ALL YOUR<br>HOME CLEANING NEEDS</h1>

  <svg class="cta-disc" viewBox="0 0 936 1324" width="936" height="1324" aria-hidden="true">
    <circle cx="991" cy="662" r="392" fill="var(--ring-grey)" opacity="0.6"/>
    <circle cx="991" cy="662" r="380" fill="var(--panel-grey)"/>
  </svg>
  <div class="cta-text">CALL<br>NOW<br>TO<br>BOOK</div>

  <div class="service-photo photo-carpet" role="img" aria-label="Photo of a carpet cleaning wand on beige carpet"></div>
  <div class="service-photo photo-upholstery" role="img" aria-label="Photo of striped upholstery being cleaned"></div>
  <div class="service-photo photo-drapery" role="img" aria-label="Photo of a technician cleaning draperies at a window"></div>
  <div class="service-photo photo-tile" role="img" aria-label="Photo of tile and grout before and after cleaning"></div>
  <div class="service-photo photo-stone" role="img" aria-label="Photo of a polished natural stone floor"></div>

  <section class="service service-carpet">
    <h2 class="service-title">CARPET CLEANING</h2>
    <p class="service-copy">Don't let dirty carpets spoil the look of your<br>beautiful home! Given our 37 years of carpet<br>cleaning experience, you can expect your<br>carpets to look fresh and new in most cases.</p>
  </section>
  <section class="service service-upholstery">
    <h2 class="service-title">UPHOLSTERY CLEANING</h2>
    <p class="service-copy">Everyday use leaves your sofas and chairs<br>looking dirty and possibly smelling of pets<br>odors. Our best method of dry cleaning or<br>shampoo and rinse extraction will leave your<br>fabrics feeling as nice as clean sheets.</p>
  </section>
  <section class="service service-drapery">
    <h2 class="service-title">DARAPERY CLEANING</h2>
    <p class="service-copy">Draperies can act as a filter, attracting<br>atmospheric soil, making them look dingy. We<br>make cleaning them easy with our safe and<br>effective in-home dry cleaning so your draperies<br>are beautiful again.</p>
  </section>
  <section class="service service-tile">
    <h2 class="service-title">TILE &amp; GROUT CLEANING</h2>
    <p class="service-copy">Tile &amp; grout get neglected. Dirty grout can lead to<br>permanent staining. Let our professionals bring back<br>the sparkle of a new floor and seal in that look.</p>
  </section>
  <section class="service service-stone">
    <h2 class="service-title">NATURAL STONE CLEANING &amp; POLISHING</h2>
    <p class="service-copy">With our state-of-the-art treatment you'll see<br>even dull, stained, scratched travertine, marble,<br>granite or other natural stone can be revitalized<br>to look new again.</p>
  </section>
</main>
</body>
</html>
```